Vellmora Harvest Online organic artisan and gourmet supermarket

Brief:
Brand: Vellmora Harvest (VH) is an online store selling artisan and organinc Italian products. Our look and feel we have gone with is rustic, premium and unfiltered (visit us @ www.vellmoraharvest.com.au)
Our slogan: "cook Italy, eat Italy, love Italy"
Goals: prior to our online store going live, we used to attend a food market once a week. Due to unfortunate circumstances, we stopped. Since then, our store has gone live and wanted to use the card as a reminder we are back at the markets.
I also have a restaurant, "vellmora ristorante" so I wanted to hand them out to customers in the restaurant but also act as reminder of our pop up market stores and our website to buy from.
Personality: VH is more than just a store. Our goal is to be not only a store but an informationa hub of Italian food.
We offer assistance to people who need help in their kitchen as well as catering
Logo: I have a logo which I was not able to upload.

Target Market(s)

Food lovers
Italian food interest
Wealthy
Organic gourmet food enthusiest

Industry/Entity Type

Store

Contact Information for Business Card

Shop online or visit us @ Birchwell Hollow organic market
Ciao@vellmoraharvest.com.au
Www.vellmoraharvest.com.au

Online store, Cooking advice, catering, ristorante and information hub

Requirements
Must have
• Logo
• Information
• May be larger than a business card to fit information but smaller than a post card
• Need to look interesting and different
• Not a simple card design
Nice to have
• Different fonts
• Rustic looking
• Qwerky

```html
<!DOCTYPE html>
<html lang="en">
<head>
<meta charset="utf-8">
<title>Vellmora Harvest – Business Cards</title>
<link rel="stylesheet" href="https://fonts.googleapis.com/css2?family=Cinzel:wght@500;700&family=Montserrat:wght@400;700&display=swap">
<style>
  :root {
    --stage: #2b2b2b;
    --card-black: #050505;
    --brand-red: #d21f26;
    --brand-green: #0f7d3c;
    --ink-white: #ffffff;
    --card-w: 680px;
    --card-h: 390px;
  }
  * { margin: 0; padding: 0; box-sizing: border-box; }
  html, body { width: 1200px; height: 900px; overflow: hidden; }
  body { background: var(--stage); font-family: "Montserrat", Arial, sans-serif; position: relative; }

  .card {
    position: absolute;
    width: var(--card-w);
    height: var(--card-h);
    background: var(--card-black);
    border-radius: 22px;
    overflow: hidden;
    box-shadow: 0 18px 40px rgba(0,0,0,.55);
  }
  .card--front { left: 80px; top: 60px; }
  .card--back { left: 440px; top: 460px; }

  .card__bands { position: absolute; inset: 0; width: 100%; height: 100%; }
  .band--red { fill: var(--brand-red); }
  .band--green { fill: var(--brand-green); }

  .brand-seal {
    position: absolute;
    border: 2px solid var(--ink-white);
    border-radius: 50%;
    display: flex;
    align-items: center;
    justify-content: center;
    text-align: center;
  }
  .brand-seal__name {
    color: var(--ink-white);
    font-family: "Montserrat", Arial, sans-serif;
    font-weight: 700;
    text-transform: uppercase;
    letter-spacing: 2px;
    line-height: 1.25;
  }
  .card--front .brand-seal { left: 36px; top: 180px; width: 140px; height: 140px; }
  .card--front .brand-seal__name { font-size: 13px; }
  .card--back .brand-seal { left: 48px; top: 60px; width: 220px; height: 220px; }
  .card--back .brand-seal__name { font-size: 20px; letter-spacing: 3px; }

  .venue-name {
    position: absolute;
    right: 40px; top: 165px;
    color: var(--ink-white);
    font-weight: 700;
    font-size: 22px;
    letter-spacing: 1.5px;
    text-transform: uppercase;
  }
  .web-line {
    position: absolute;
    right: 34px; top: 300px;
    color: var(--ink-white);
    font-size: 14px;
    letter-spacing: .5px;
    text-transform: uppercase;
  }

  .person { position: absolute; right: 36px; top: 36px; text-align: right; }
  .person__name {
    font-family: "Cinzel", Georgia, serif;
    font-weight: 500;
    color: var(--brand-red);
    font-size: 30px;
    letter-spacing: 1px;
    line-height: 1;
  }
  .person__role {
    color: var(--ink-white);
    font-size: 13px;
    letter-spacing: 1px;
    margin-top: 4px;
    text-transform: uppercase;
  }

  .slogan {
    position: absolute;
    right: 36px; top: 205px;
    color: var(--ink-white);
    font-family: "Cinzel", Georgia, serif;
    font-weight: 700;
    font-size: 17px;
    letter-spacing: .5px;
  }

  .contact-list {
    position: absolute;
    left: 30px; top: 312px;
    list-style: none;
    color: var(--ink-white);
    font-size: 14px;
    letter-spacing: .5px;
    text-transform: uppercase;
  }
  .contact-list li { display: flex; align-items: center; gap: 9px; line-height: 22px; }
  .contact-list svg { width: 13px; height: 13px; fill: none; stroke: var(--ink-white); stroke-width: 2; }
</style>
</head>
<body>

  <section class="card card--front">
    <svg class="card__bands" viewBox="0 0 680 390" preserveAspectRatio="none" aria-hidden="true">
      <polygon class="band--green" points="0,340 402,340 395,390 0,390"/>
      <polygon class="band--red" points="420,210 680,210 680,390 395,390"/>
    </svg>
    <div class="brand-seal"><span class="brand-seal__name">Vellmora<br>Harvest</span></div>
    <h2 class="venue-name">Vellmora Ristorante</h2>
    <p class="web-line">www.vellmoraharvest.com.au</p>
  </section>

  <section class="card card--back">
    <svg class="card__bands" viewBox="0 0 680 390" preserveAspectRatio="none" aria-hidden="true">
      <polygon class="band--green" points="380,300 680,268 680,322 440,360"/>
      <polygon class="band--red" points="0,300 400,300 480,390 0,390"/>
    </svg>
    <div class="brand-seal"><span class="brand-seal__name">Vellmora<br>Harvest</span></div>
    <div class="person">
      <h1 class="person__name">Lorena Vasquet</h1>
      <p class="person__role">Director</p>
    </div>
    <p class="slogan">Cook Italy, Eat Italy, Love Italy</p>
    <ul class="contact-list">
      <li><svg viewBox="0 0 16 16"><path d="M4 1.5l2.5 3-1.5 1.8a9 9 0 0 0 4.7 4.7l1.8-1.5 3 2.5-1.6 2.5C7.5 14.5 1.5 8.5 1.5 3.1z"/></svg>303-555-0186</li>
      <li><svg viewBox="0 0 16 16"><rect x="1.5" y="3.5" width="13" height="9"/><path d="M1.5 3.5l6.5 5 6.5-5"/></svg>info@vellmoraharvest.com.au</li>
      <li><svg viewBox="0 0 16 16"><circle cx="8" cy="8" r="6.5"/><path d="M1.5 8h13M8 1.5c3 3.5 3 9.5 0 13M8 1.5c-3 3.5-3 9.5 0 13"/></svg>www.vellmoraharvest.com.au</li>
    </ul>
  </section>

</body>
</html>
```